Letterhead for 3 attorney Workers' Comp law firm

We are a 3 attorney law office. We specialize in Workers' Compensation. Our office represents workers who are injured on the job, and the estates of workers who are killed one the job.
When we started our office, we created our own letterhead & have been using it for years. We've just recently hired the 3rd attorney, and were going to just add his name to the letterhead, but have decided we wanted to get a professionally designed letterhead and business cards at this point.
We want something that looks clean and professional. It must look good in black and white because we often make multiple copies of our documents. We're hoping for a design that resonates confidence, reliability and experience.
The design must include the firm name: Dorrance & Pike, PLLC. We would like the PLLC to be small compared to the Dorrance & Pike graphic. We also want to incorporate the attorney names: Ulric Dorrance, Janet Pike, and Lyle Hagberg. Our current letterhead has our contact info in the footer at the bottom of the page. We like that design, but are open to the idea of having it at the top. We'll leave that at the discretion of the designer. Our contact info is as follows: 472 S. Larchmont Avenue, Suite 315 Bellingham, WA 98117 Phone: 360-514-2967, Fax: 360-521-6079, and our website: www.dorrancepike-law.example
Target Market(s)
Clients, courts, other legal offices, doctors offices. These are the people who see our letterhead most frequently. It's not so much for marketing purposes, mainly so that we have a professional image when sending out documents.
Industry/Entity Type
Law Firm
Contact Information for Business Card
On the back of the business card: it can be designed, or be a template for filling in appointment reminder information (i.e. date, time, etc)
Colors
Designer to choose colors to be used in the design.
Requirements
Must have
- Must have our firm name at the top.
- Must include the attorney names.
- Must have all of our contact information (can be at top or bottom - whatever looks best with the design)
Nice to have
- A strong, confident design
Should not have
- We don't want the design to be playful, cartoony or busy.

```html
<!DOCTYPE html>
<html lang="en">
<head>
<meta charset="utf-8">
<title>Dorrance &amp; Pike, PLLC — Stationery</title>
<link rel="stylesheet" href="https://fonts.googleapis.com/css2?family=Questrial&family=Arimo:wght@400&family=Parisienne&display=swap">
<style>
  :root{
    --backdrop:#c2c2c6;
    --paper:#ffffff;
    --navy:#2f4774;
    --navy-deep:#23376a;
    --ink:#5a5a5e;
    --ink-soft:#77777b;
    --headline-blue:#1f74c4;
    --card-text:#8592ad;
    --card-label:#ffffff;
  }
  *{margin:0;padding:0;box-sizing:border-box}
  html,body{width:1200px;height:1200px;overflow:hidden}
  body{background:var(--backdrop);position:relative;font-family:"Questrial",sans-serif}

  /* Letterhead */
  .letterhead{position:absolute;left:198px;top:213px;width:512px;height:723px;background:var(--paper)}
  .brand{position:absolute;display:flex;align-items:center;gap:10px}
  .letterhead .brand{left:18px;top:46px}
  .brand-square{width:40px;height:40px;background:var(--navy-deep)}
  .brand-name{font-family:"Questrial",sans-serif;color:var(--ink-soft);line-height:1}
  .letterhead .brand-name{font-size:20px}
  .brand-name small{font-size:10px;letter-spacing:.5px}

  .headline{position:absolute;left:0;right:0;top:128px;text-align:center;font-size:22px;letter-spacing:.5px;color:var(--ink);padding-left:2px}
  .headline span{color:var(--headline-blue)}
  .subhead{position:absolute;left:162px;top:162px;width:200px;font-family:"Arimo",sans-serif;font-size:8.5px;line-height:10.5px;color:var(--ink)}

  .body-copy{position:absolute;left:76px;top:213px;width:366px;font-size:10.6px;line-height:14.6px;letter-spacing:.55px;color:var(--ink)}
  .body-copy p{margin-bottom:14.6px}

  .signature{position:absolute;left:76px;top:526px;font-family:"Parisienne",cursive;font-size:20px;color:var(--ink-soft);border-bottom:1px solid #b9b9bc;line-height:24px;padding-right:2px}

  .contact{position:absolute;left:355px;top:609px;border-left:1.5px solid var(--navy-deep);padding-left:9px;font-family:"Arimo",sans-serif;font-size:8.8px;line-height:13.6px;color:var(--ink)}
  .contact .label{color:var(--navy-deep)}
  .contact .address{line-height:10.5px;margin-top:1px}

  /* Business cards */
  .card{position:absolute;left:796px;width:219px;height:122px;background:var(--navy)}
  .card-front{top:411px}
  .card-back{top:601px}
  .card-contact{position:absolute;left:97px;top:36px;border-left:1px solid #c9d0de;padding-left:8px;font-family:"Arimo",sans-serif;font-size:6.4px;line-height:10px;color:var(--card-text);white-space:nowrap}
  .card-contact .label{color:var(--card-label)}
  .card-address{position:absolute;left:0;right:0;bottom:3px;text-align:center;font-family:"Arimo",sans-serif;font-size:6.4px;color:var(--card-label)}
  .card-back .brand{left:10px;top:88px;gap:6px}
  .card-back .brand-square{width:20px;height:20px;background:#8a97b3}
  .card-back .brand-name{font-size:9px;color:#9aa5bd}
  .card-back .brand-name small{font-size:5px}
</style>
</head>
<body>

<section class="letterhead" aria-label="Letterhead">
  <div class="brand">
    <div class="brand-square"></div>
    <div class="brand-name">Dorrance &amp; Pike, <small>PLLC</small></div>
  </div>

  <h1 class="headline">YOUR<span>HEADLINE</span></h1>
  <p class="subhead">Lorem ipsum dolor sit amet, consectetuer adipi-<br>scing elit, sed diam</p>

  <div class="body-copy">
    <p>Lorem ipsum dolor sit amet, consectetuer adipiscing elit, sed diam nonummy nibh euismod tincidunt ut laoreet dolore magna aliquam erat volutpat. Ut wisi enim ad minim veniam, quis nostrud exerci tation ullamcorper suscipit lobortis nisl ut aliquip ex ea commodo consequat. Duis autem vel eum iriure dolor in hendrerit in vulputate velit esse molestie consequat, vel illum dolore eu feugiat nulla facilisis at vero eros et accumsan et iusto odio dignissim qui bladit praesent luptatum zzril delenit augue duis dolore te feugait nulla facilisi.</p>
    <p>Nam liber tempor cum soluta nobis eleifend option congue nihil imperdiet doming id quod mazim placerat facer possim assum. Typi non habent claritatem insitam; est usus legentis in iis qui facit eorum claritatem. Investigationes demonstraverunt lectores legere me lius quod ii legunt saepius. Claritas est etiam processus dynamicus, qui sequitur mutationem consuetudium lectorum.</p>
    <p>Mirum est notare quam littera gothica, quam nunc putamus parum claram, anteposuerit litterarum formas humanitatis per seacula quarta decima et quinta decima. Eodem modo typi, qui nunc nobis videntur parum clari, fiant sollemnes in futurum.</p>
  </div>

  <div class="signature">Signature</div>

  <address class="contact">
    Ulric Dorrance<br>
    Janet Pike<br>
    Lyle Hagberg<br>
    <span class="label">Phone:</span> 360-514-2967<br>
    <span class="label">Fax:</span> 360-521-6079<br>
    <span class="label">Web:</span> www.dorrancepike-law.example
    <div class="address"><span class="label">Address:</span> 472 S. Larchmont Avenue,<br>Suite 315 Bellingham, WA 98117</div>
  </address>
</section>

<section class="card card-front" aria-label="Business card front">
  <div class="card-contact">
    Ulric Dorrance<br>
    Janet Pike<br>
    Lyle Hagberg<br>
    <span class="label">Phone:</span> 360-514-2967<br>
    <span class="label">Fax:</span> 360-521-6079<br>
    <span class="label">Web:</span> www.dorrancepike-law.example
  </div>
  <div class="card-address">472 S. Larchmont Avenue, Suite 315 Bellingham, WA 98117</div>
</section>

<section class="card card-back" aria-label="Business card back">
  <div class="brand">
    <div class="brand-square"></div>
    <div class="brand-name">Dorrance &amp; Pike, <small>PLLC</small></div>
  </div>
</section>

</body>
</html>
```